EXPEDITE! Business Card For a Private Equity Firm
Fresh and Sleek
EXPEDITE!  Business Card For a Private Equity Firm - Financial Services
Creative Brief
Bright & Fun-filled
Ned Rusholt
Managing Partner
712 Larkmoor Street New York, NY 10032
ned@vorumbra-example.com
www.vorumbra-example.com
Looking for a fresh look on our new business cards. We have had previous designs on Plenavox for similar companies, but, now is time to refresh the look! Please submit as many design as possible. We will give you fast, efficient feedback!
Vorumbra Vorumbra
All. We also need email signatures and letterhead. Please provide.

```html
<!DOCTYPE html>
<html lang="en">
<head>
<meta charset="utf-8">
<title>Vorumbra Business Card</title>
<link rel="stylesheet" href="https://fonts.googleapis.com/css2?family=Cinzel:wght@500&family=Lato:ital,wght@0,300;0,400;1,300&display=swap">
<style>
  :root {
    --page-bg: #e4e4e2;
    --card-white: #fbfbfb;
    --navy-deep: #0b2350;
    --navy: #163f86;
    --blue: #2a6cc0;
    --blue-bright: #3f8ede;
    --text-grey: #5a5e66;
    --rule-grey: #c9ccd1;
    --white: #ffffff;
  }
  * { box-sizing: border-box; margin: 0; padding: 0; }
  html, body { width: 1200px; height: 840px; overflow: hidden; }
  body {
    background: var(--page-bg);
    font-family: "Lato", Arial, sans-serif;
    position: relative;
  }
  .card {
    position: absolute;
    width: 525px;
    height: 300px;
    top: 270px;
    box-shadow: 0 6px 18px rgba(0,0,0,0.18);
    overflow: hidden;
  }
  /* Front card */
  .card-front { left: 45px; background: var(--card-white); }
  .front-graphics { position: absolute; left: 0; top: 0; width: 525px; height: 300px; }
  .brand {
    position: absolute; left: 38px; top: 36px;
    display: flex; align-items: center; gap: 12px;
  }
  .brand-dot {
    width: 22px; height: 22px; border-radius: 50%;
    background: var(--blue);
  }
  .brand-name {
    font-family: "Cinzel", Georgia, serif;
    font-weight: 500;
    font-size: 34px;
    letter-spacing: 1px;
    color: var(--navy);
  }
  .contact-list {
    position: absolute; left: 40px; top: 100px;
    list-style: none;
    font-size: 11px; line-height: 17px;
    color: var(--text-grey);
  }
  .contact-list li { display: flex; align-items: center; gap: 7px; }
  .contact-list .address { padding-left: 17px; }
  .contact-list svg { width: 10px; height: 10px; flex: none; }
  .front-web {
    position: absolute; left: 28px; top: 195px;
    height: 27px; line-height: 27px;
    font-size: 11px; letter-spacing: 0.5px; color: var(--white);
    white-space: nowrap;
  }
  .person {
    position: absolute; right: 40px; top: 197px; text-align: left;
  }
  .person-name {
    font-weight: 300; font-style: italic;
    font-size: 18px; color: var(--text-grey);
  }
  .person-title { font-size: 11px; color: var(--blue); margin-top: 2px; }

  /* Back card */
  .card-back {
    left: 630px;
    background: radial-gradient(ellipse at 25% 30%, var(--blue-bright) 0%, var(--blue) 30%, var(--navy) 65%, var(--navy-deep) 100%);
  }
  .back-brand {
    position: absolute; right: 42px; top: 118px;
    text-align: right;
  }
  .back-brand-row { display: flex; align-items: center; gap: 12px; justify-content: flex-end; }
  .back-brand .brand-dot { background: var(--white); }
  .back-brand .brand-name { color: var(--white); font-size: 38px; }
  .back-web {
    font-size: 11px; letter-spacing: 2px; color: #cfe0f5; margin-top: 2px;
  }
</style>
</head>
<body>
  <section class="card card-front">
    <svg class="front-graphics" viewBox="0 0 525 300" aria-hidden="true">
      <path d="M0 195 L198 195 Q213 195 219 210 L226 228 Q217 222 200 222 L0 222 Z" fill="#2a6cc0"/>
      <path d="M219 210 Q232 246 272 246 L525 246" fill="none" stroke="#c9ccd1" stroke-width="1.5"/>
      <path d="M0 290 L525 290" stroke="#e2e4e8" stroke-width="1"/>
    </svg>
    <div class="brand">
      <span class="brand-dot"></span>
      <span class="brand-name">VORUMBRA</span>
    </div>
    <ul class="contact-list">
      <li class="address">712 Larkmoor Street</li>
      <li class="address">New York, NY 10032</li>
      <li><svg viewBox="0 0 10 10"><rect x="0" y="0" width="10" height="10" rx="2" fill="#2a6cc0"/><path d="M3 2.5 L4.2 2.5 L4.6 4 L3.9 4.6 Q4.6 6 5.6 6.3 L6.2 5.6 L7.6 6 L7.6 7.3 Q4 7.6 2.7 3.3Z" fill="#fff"/></svg>(555) 014-2290</li>
      <li><svg viewBox="0 0 10 10"><rect x="0" y="0" width="10" height="10" rx="2" fill="#2a6cc0"/><rect x="2.5" y="4" width="5" height="3.5" fill="#fff"/><rect x="3.3" y="2.2" width="3.4" height="1.6" fill="#fff"/></svg>(555) 014-2291</li>
      <li><svg viewBox="0 0 10 10"><rect x="0" y="0" width="10" height="10" rx="2" fill="#2a6cc0"/><rect x="2" y="3" width="6" height="4" fill="none" stroke="#fff" stroke-width="0.8"/><path d="M2 3 L5 5.3 L8 3" fill="none" stroke="#fff" stroke-width="0.8"/></svg>ned@vorumbra-example.com</li>
    </ul>
    <div class="front-web">www.vorumbra-example.com</div>
    <div class="person">
      <div class="person-name">Ned Rusholt</div>
      <div class="person-title">Managing Partner</div>
    </div>
  </section>

  <section class="card card-back">
    <div class="back-brand">
      <div class="back-brand-row">
        <span class="brand-dot"></span>
        <span class="brand-name">VORUMBRA</span>
      </div>
      <div class="back-web">www.vorumbra-example.com</div>
    </div>
  </section>
</body>
</html>
```